Flyer / Mailer for Business Debt Relief Business - Tillbrook Partners 6" x 11"

We need a 6" x 11" double sided flyer. This will be sent out to potential customers with high interest business loans. We would like the design to coordinate with the colors of our logo. I have included a mock up that we sketched out. I have also included a file of a mailer we received that we would like to use as a template (not colors or fonts, just set up). I have also included an .ai file of our logo.

```html
<!DOCTYPE html>
<html lang="en">
<head>
<meta charset="utf-8">
<title>Tillbrook Partners – Business Debt Relief Mailer</title>
<link href="https://fonts.googleapis.com/css2?family=Roboto:wght@300;400;500;700&display=swap" rel="stylesheet">
<style>
  :root {
    --brand-green: #6aa83c;
    --brand-blue: #0a7ac4;
    --heading-blue: #1477c0;
    --ink: #2d2d2d;
    --footer-grey: #474747;
    --panel-grey: #e6e6e6;
    --page-bg: #3a3a3a;
    --paper: #ffffff;
    --link-blue: #3fb0ee;
  }
  html, body {
    margin: 0;
    padding: 0;
    width: 1200px;
    height: 1200px;
    overflow: hidden;
    background: var(--page-bg);
    font-family: "Roboto", Arial, sans-serif;
  }
  .canvas { position: relative; width: 1200px; height: 1200px; }
  .mailer-side {
    position: absolute;
    width: 906px;
    height: 494px;
    background: var(--paper);
    box-shadow: 0 8px 20px rgba(0,0,0,.45);
  }
  .mailer-side svg { display: block; width: 100%; height: 100%; }
  .mailer-front { left: 134px; top: 86px; }
  .mailer-back  { left: 138px; top: 636px; }
  .t-white { fill: #fff; }
  .t-bold { font-weight: 700; }
  .t-medium { font-weight: 500; }
  .t-body { font-weight: 400; fill: var(--ink); }
  .t-blue { fill: var(--heading-blue); }
  .t-link { fill: var(--link-blue); }
  .brand-name { font-weight: 300; fill: var(--ink); letter-spacing: 2px; }
  .brand-sub { font-weight: 300; fill: var(--ink); letter-spacing: 6px; }
</style>
</head>
<body>
<main class="canvas">

  <!-- Front side -->
  <section class="mailer-side mailer-front">
    <svg viewBox="0 0 1133 618" xmlns="http://www.w3.org/2000/svg">
      <defs>
        <linearGradient id="photoGreen" x1="0" y1="0" x2="1" y2="1">
          <stop offset="0" stop-color="#7fa35e"/><stop offset="1" stop-color="#c9c2b4"/>
        </linearGradient>
        <linearGradient id="photoDesk" x1="0" y1="0" x2="1" y2="1">
          <stop offset="0" stop-color="#eef0f2"/><stop offset="1" stop-color="#b9bcc0"/>
        </linearGradient>
        <linearGradient id="photoChart" x1="0" y1="0" x2="1" y2="1">
          <stop offset="0" stop-color="#233038"/><stop offset="1" stop-color="#4d6a72"/>
        </linearGradient>
        <linearGradient id="photoPerson" x1="0" y1="0" x2="0" y2="1">
          <stop offset="0" stop-color="#e8e8e8" stop-opacity="0"/><stop offset=".35" stop-color="#b49a88"/><stop offset="1" stop-color="#1e1e1e"/>
        </linearGradient>
      </defs>

      <!-- photo column -->
      <rect x="0" y="0" width="226" height="165" fill="url(#photoGreen)" role="img" aria-label="Hand dropping a coin into a jar with a growing plant"/>
      <rect x="0" y="172" width="226" height="315" fill="url(#photoDesk)" role="img" aria-label="Person working at a laptop with paperwork, coins and a calculator"/>
      <rect x="0" y="487" width="226" height="131" fill="url(#photoChart)" role="img" aria-label="Hand drawing a glowing bar chart"/>

      <!-- header bands -->
      <rect class="band-green" x="247" y="0" width="886" height="87" fill="var(--brand-green)"/>
      <text class="t-white t-bold" x="268" y="56" font-size="34">HELPING BUSSINESS FOCUS ON WANT MATTERS</text>

      <polygon class="band-blue" points="247,92 1133,92 1133,155 795,155 778,190 247,190" fill="var(--brand-blue)"/>
      <text class="t-white t-medium" x="270" y="132" font-size="21">WE UNDERSTAND THAT MERCHANT CASH ADVANCE LOANS CAN BE  A BURDEN</text>
      <text class="t-white t-bold" x="278" y="168" font-size="30">ON YOUR BUSINESS</text>

      <polygon points="247,199 755,199 753,205 247,205" fill="var(--brand-green)"/>
      <polygon points="791,162 1133,162 1133,168 795,168 787,190 782,190" fill="var(--brand-green)"/>

      <text class="t-blue t-bold" x="260" y="267" font-size="23">OVER WHELMED BY DAILY / WEEKLY PAYMENT?</text>

      <polygon points="257,296 445,296 478,342 257,342" fill="var(--brand-green)"/>
      <text class="t-white t-bold" x="265" y="331" font-size="24">WE CAN HELP !</text>

      <!-- brand name -->
      <rect x="922" y="210" width="46" height="46" fill="var(--brand-green)"/>
      <text class="brand-name" x="947" y="308" font-size="22" text-anchor="middle">TILLBROOK PARTNERS</text>
      <text class="brand-sub" x="947" y="326" font-size="11" text-anchor="middle">CONSULTING</text>

      <!-- benefits panel -->
      <rect x="258" y="355" width="875" height="163" fill="var(--panel-grey)"/>
      <g class="benefits-left" font-size="14.5">
        <circle cx="281" cy="383" r="3.5" fill="var(--brand-blue)"/><text class="t-body" x="294" y="388">This is not a loan,we are not lenders.</text>
        <circle cx="281" cy="410" r="3.5" fill="var(--brand-blue)"/><text class="t-body" x="294" y="415">Improve your business cash flow immedictely</text>
        <circle cx="281" cy="437" r="3.5" fill="var(--brand-blue)"/><text class="t-body" x="294" y="442">Move payments to one monthly amount</text>
        <circle cx="281" cy="465" r="3.5" fill="var(--brand-blue)"/><text class="t-body" x="294" y="470">Reduce the amount you are paying out monthly</text>
        <circle cx="281" cy="492" r="3.5" fill="var(--brand-blue)"/><text class="t-body" x="294" y="497">Stratesic alternetives to his interest loans</text>
      </g>
      <line x1="604" y1="378" x2="604" y2="500" stroke="#555" stroke-width="1.2"/>
      <g class="benefits-right" font-size="14.5">
        <circle cx="631" cy="386" r="3.5" fill="var(--brand-blue)"/><text class="t-body" x="651" y="392">Fast, confidential business debt relief</text>
        <circle cx="631" cy="413" r="3.5" fill="var(--brand-blue)"/><text class="t-body" x="651" y="419">No- oblisetion consultation</text>
        <circle cx="631" cy="440" r="3.5" fill="var(--brand-blue)"/><text class="t-body" x="651" y="446">Absolutely no credit pulls</text>
        <circle cx="631" cy="467" r="3.5" fill="var(--brand-blue)"/><text class="t-body" x="651" y="473">No colleteral, no financials</text>
      </g>

      <!-- footer -->
      <rect x="235" y="535" width="898" height="83" fill="var(--footer-grey)"/>
      <text x="258" y="563" font-size="13" class="t-white t-medium">visit our website : <tspan class="t-link">www.tillbrookpartners.com</tspan> /  call now for free consvltation with our experts</text>
      <path d="M259 578 q2 -2 4 0 l2 3 q1 1 0 2 l-1 1 q2 4 5 5 l1 -1 q1 -1 2 0 l3 2 q2 2 0 4 q-3 3 -8 -1 q-6 -5 -8 -11 q-1 -3 0 -4z" fill="#fff"/>
      <text x="276" y="589" font-size="14" class="t-white t-medium">555-218-0417</text>
      <rect x="390" y="580" width="10" height="7" rx="1" fill="none" stroke="#fff" stroke-width="1.3"/>
      <polyline points="390,580 395,584 400,580" fill="none" stroke="#fff" stroke-width="1.2"/>
      <text x="410" y="588" font-size="14" class="t-white t-medium">info@tillbrookpartners.com</text>

      <!-- consultant portrait area -->
      <path d="M885 618 L900 520 Q930 470 990 460 L990 340 L1080 340 L1080 460 Q1115 470 1130 520 L1133 618 Z" fill="url(#photoPerson)" role="img" aria-label="Portrait of a smiling consultant in a dark business suit"/>
    </svg>
  </section>

  <!-- Back side -->
  <section class="mailer-side mailer-back">
    <svg viewBox="0 0 1133 618" xmlns="http://www.w3.org/2000/svg">
      <polygon points="0,0 1133,0 1133,36 523,36 505,70 0,70" fill="var(--brand-blue)"/>
      <polygon points="532,46 1133,46 1133,57 527,57" fill="var(--brand-green)"/>
      <polygon points="0,80 455,80 450,92 0,92" fill="var(--brand-green)"/>

      <rect x="214" y="128" width="46" height="46" fill="var(--brand-green)"/>
      <text class="brand-name" x="240" y="219" font-size="22" text-anchor="middle">TILLBROOK PARTNERS</text>
      <text class="brand-sub" x="240" y="236" font-size="11" text-anchor="middle">CONSULTING</text>

      <text x="52" y="284" font-size="22" font-weight="500" fill="var(--ink)">418 n harlow ave denbury,TX-75120</text>

      <rect x="0" y="308" width="495" height="110" fill="var(--brand-green)"/>
      <text class="t-white t-medium" x="228" y="352" font-size="24" text-anchor="middle">STRETESIC DEBT RELIEF</text>
      <text class="t-white t-medium" x="231" y="383" font-size="24" text-anchor="middle">FOR BUSINESSES OF ALL SIZES</text>

      <rect x="0" y="424" width="495" height="151" fill="var(--brand-blue)"/>
      <text class="t-white t-medium" x="35" y="486" font-size="18" textLength="403">Stop taking out loans to pay off other loans</text>
      <text class="t-white t-medium" x="35" y="509" font-size="18">Take back your business cash flow,  and focus on</text>
      <text class="t-white t-medium" x="35" y="531" font-size="18">what matters.</text>

      <polygon points="0,590 480,590 505,618 0,618" fill="var(--footer-grey)"/>
      <polygon points="480,590 490,590 515,612 930,612 925,618 505,618" fill="#cfcfcf"/>
      <text class="t-white" x="75" y="609" font-size="15" letter-spacing="2">www.tillbrookpartners.com</text>

      <rect x="957" y="93" width="140" height="139" fill="#e2e2e2" stroke="#fff" stroke-width="4" stroke-dasharray="4 4"/>

      <g stroke="#777" stroke-width="1.2">
        <line x1="696" y1="329" x2="1090" y2="329"/>
        <line x1="693" y1="387" x2="1087" y2="387"/>
        <line x1="696" y1="452" x2="1090" y2="452"/>
        <line x1="689" y1="518" x2="1083" y2="518"/>
      </g>

      <polygon points="1118,438 1133,426 1133,618 938,618 950,605 1118,605" fill="var(--brand-green)"/>
    </svg>
  </section>

</main>
</body>
</html>
```